Tobin's Jewelry Studio Needs a Moving Location Flyer

We need a flyer to inform our customers of our location moving. We will be moving to our city's downtown which is only 1 mile away from our current address. We will be having a moving sale ( Up to 80% off). The sale starts Sept. 8th Our business creates, sells, and repairs fine jewelry. Dimensions are 5"x8"

Target Market(s)

Women ages 25-55

Industry/Entity Type

Jewelry

Colors
85abd2
cfdeed

Requirements
Must have
• Our logo
• Mention of the sale
• Our current address
• 4785 Cresthaven Blvd.
• Dunmore, Ca 94318
• (415)826-3319
Nice to have
• Mention that we're relocating to downtown Dunmore (new location opening Nov. 1st.)

```html
<!DOCTYPE html>
<html lang="en">
<head>
<meta charset="utf-8">
<title>Tobin's Jewelry Studio – Moving Sale Flyer</title>
<link rel="stylesheet" href="https://fonts.googleapis.com/css2?family=Arimo:wght@400;700&display=swap">
<style>
  :root {
    --sky-light: #7fd8f2;
    --sky-mid: #5ab8ea;
    --sky-deep: #4798dc;
    --band-light: #3fc9f1;
    --band-deep: #137fe0;
    --headline-blue: #2b58b6;
    --body-blue: #1a4ccc;
    --white: #ffffff;
    --ink: #111111;
    --silver: #d7dde2;
    --dial-light: #f1f2f3;
    --dial-mid: #c9ccd0;
    --dial-rim: #8d9298;
    --badge: #bfe6f2;
  }
  * { margin: 0; padding: 0; box-sizing: border-box; }
  html, body { width: 1200px; height: 751px; overflow: hidden; }
  body { font-family: "Arimo", Arial, sans-serif; }

  .flyer {
    position: relative;
    width: 1200px;
    height: 751px;
    overflow: hidden;
    background: radial-gradient(ellipse 620px 520px at 470px 240px, var(--sky-light) 0%, var(--sky-mid) 55%, var(--sky-deep) 100%);
  }

  .contact-band {
    position: absolute;
    left: 0; top: 512px;
    width: 1200px; height: 239px;
    background: radial-gradient(ellipse 520px 330px at 470px 120px, var(--band-light) 0%, #239ee8 55%, var(--band-deep) 100%);
  }
  .band-edge {
    position: absolute;
    left: 470px; top: 510px;
    width: 730px; height: 3px;
    background: linear-gradient(90deg, rgba(215,221,226,0) 0%, var(--silver) 20%, var(--silver) 100%);
  }

  .compass-art {
    position: absolute;
    left: -85px; top: 170px;
    width: 550px; height: 550px;
    border-radius: 50%;
    background: radial-gradient(circle at 50% 50%, var(--dial-light) 0%, #e2e4e6 70%, var(--dial-mid) 88%, var(--dial-rim) 100%);
    box-shadow: 0 6px 18px rgba(0, 40, 90, 0.35);
  }

  .message {
    position: absolute;
    left: 500px; width: 630px;
    text-align: center;
    font-weight: 700;
    line-height: 1.15;
  }
  .lead { top: 70px; font-size: 30px; color: var(--headline-blue); }
  .city { top: 124px; font-size: 52px; color: var(--headline-blue); }
  .opening { top: 188px; font-size: 30px; color: var(--headline-blue); }
  .sale-date { top: 249px; font-size: 36px; color: var(--white); }
  .sale-offer { top: 313px; font-size: 29px; color: var(--white); line-height: 1.35; }
  .services { left: 470px; width: 704px; top: 429px; font-size: 21px; color: var(--body-blue); }

  .brand {
    position: absolute;
    left: 500px; width: 630px; top: 568px;
    display: flex; align-items: center; justify-content: center; gap: 14px;
  }
  .brand-mark {
    width: 42px; height: 42px; border-radius: 50%;
    background: var(--badge);
  }
  .brand-name {
    font-size: 24px; font-weight: 700; color: var(--ink);
  }

  .address, .phone {
    position: absolute;
    left: 500px; width: 630px;
    text-align: center;
    font-size: 22px; color: var(--ink);
  }
  .address { top: 651px; }
  .phone {
    top: 689px;
    display: flex; align-items: center; justify-content: center; gap: 8px;
  }
  .phone-icon { width: 28px; height: 28px; }
</style>
</head>
<body>
  <main class="flyer">
    <div class="contact-band"></div>
    <div class="band-edge"></div>

    <div class="compass-art" role="img" aria-label="Illustration of a silver compass whose dial reads Dunmore, with a blue and white needle"></div>

    <p class="message lead">we're relocating to downtown</p>
    <h1 class="message city">Dunmore</h1>
    <p class="message opening">(new location opening Nov. 1st.)</p>
    <p class="message sale-date">The sale starts Sept. 8th</p>
    <p class="message sale-offer">We will be having a<br>moving sale (Up to 80% off)</p>
    <p class="message services">Our business tcreates, sells, and repairs fine jewelry.</p>

    <div class="brand">
      <span class="brand-mark"></span>
      <span class="brand-name">Tobin's Jewelry Studio</span>
    </div>

    <p class="address">4785 Cresthaven Blvd., Dunmore, Ca 94318</p>
    <p class="phone">
      <svg class="phone-icon" viewBox="0 0 28 28" aria-hidden="true">
        <circle cx="14" cy="14" r="12.5" fill="none" stroke="#111" stroke-width="1.8"/>
        <path d="M9.5 7.5c.8-.6 1.8-.4 2.3.4l1.3 2.2c.4.7.2 1.6-.4 2l-1 .7c.7 1.8 1.9 3.3 3.5 4.3l.8-.9c.5-.6 1.4-.7 2-.2l2.1 1.5c.8.6.9 1.6.3 2.3l-.9 1c-.8.9-2.1 1.2-3.2.7-3.8-1.6-6.6-4.8-7.7-8.8-.3-1.2.1-2.4 1-3.1z" fill="#111"/>
      </svg>
      <span>(415)826-3319</span>
    </p>
  </main>
</body>
</html>
```